Business Card design for a skin clinic

i would like a business card design for our skin clinic.
our logo colors are Blue and Grey and Bule /white.
we are searching for a minimalistic design yet very elegant,dynamic and professional which can reflect a professional medical skin care clinic( not a beauty salon).
THE DESGIN IS NOT FOR A PERSON IT WILL BE USED IN THE CLINIC FOR CLIENTS SO THERE SHOULD BE NO NAME OF A PERSON ONLY THE CLINIC NAME AND THE CONTACT INFO

Target Market(s)
young and old womens
Industry/Entity Type
Business
Contact Information for Business Card
we have 2 address and both should be on the card.
address A: Lindenhoflaan 214B, 3041KP Rotterdam, Tel 010 483 21 95
address B: Zonnewijzerstraat 238, 1062RT Amsterdam Tel 020 571 3829
website www.huidpuntzorg.nu, email info@huidpuntzorg.nu
Look and feel
Each slider illustrates characteristics of the customer's brand and the style your logo design should communicate.

```html
<!DOCTYPE html>
<html lang="nl">
<head>
<meta charset="utf-8">
<title>Huidpuntzorg – visitekaartje</title>
<link rel="stylesheet" href="https://fonts.googleapis.com/css2?family=Jost:wght@400;500&family=Open+Sans:wght@400&family=Questrial&display=swap">
<style>
  :root {
    --stage: #ebe8e3;
    --paper: #ffffff;
    --ink-dark: #05070d;
    --brand-blue: #3a87c8;
    --blue-light: #2f95d3;
    --blue-deep: #4a85c2;
    --brand-grey: #5f5f64;
    --text-grey: #55565b;
    --text-light: #ececee;
    --link-blue: #2f9be0;
  }
  * { box-sizing: border-box; margin: 0; padding: 0; }
  html, body { width: 1200px; height: 1200px; overflow: hidden; }
  body { background: var(--stage); position: relative; font-family: "Open Sans", Arial, sans-serif; }

  .card {
    position: absolute;
    left: 242px;
    width: 715px;
    height: 406px;
    overflow: hidden;
    box-shadow: 0 6px 18px rgba(0,0,0,0.18);
  }
  .card--front { top: 140px; background: var(--paper); }
  .card--back { top: 650px; background: var(--ink-dark); }

  .card__shapes { position: absolute; inset: 0; width: 100%; height: 100%; }

  .brand { position: absolute; text-align: center; }
  .brand__name {
    font-family: "Jost", "Futura", sans-serif;
    font-weight: 500;
    letter-spacing: 0.06em;
    line-height: 1;
  }
  .brand__tagline {
    font-family: "Questrial", sans-serif;
    letter-spacing: 0.12em;
    line-height: 1;
  }

  .card--front .brand { left: 20px; width: 320px; top: 123px; }
  .card--front .brand__name { font-size: 31px; color: var(--brand-blue); }
  .card--front .brand__tagline { font-size: 13px; color: var(--text-grey); margin-top: 12px; }

  .card--back .brand { left: 0; width: 100%; top: 218px; }
  .card--back .brand__name { font-size: 40px; color: var(--text-light); }
  .card--back .brand__tagline { font-size: 16px; color: var(--text-light); margin-top: 16px; }

  .contact {
    position: absolute;
    right: 35px;
    top: 138px;
    text-align: right;
    color: #ffffff;
    font-size: 17px;
    line-height: 24px;
  }
  .contact__group + .contact__group { margin-top: 22px; }
  .contact__row { display: flex; justify-content: flex-end; align-items: center; gap: 7px; }
  .contact__icon { width: 16px; height: 16px; flex: none; }

  .website {
    position: absolute;
    left: 0;
    width: 100%;
    top: 349px;
    text-align: center;
    color: var(--link-blue);
    font-size: 17px;
  }
</style>
</head>
<body>

  <section class="card card--front" aria-label="Voorkant visitekaartje">
    <svg class="card__shapes" viewBox="0 0 572 325" preserveAspectRatio="none" aria-hidden="true">
      <defs>
        <linearGradient id="panelBlue" x1="1" y1="0" x2="0.3" y2="1">
          <stop offset="0" stop-color="var(--blue-light)"/>
          <stop offset="1" stop-color="var(--blue-deep)"/>
        </linearGradient>
      </defs>
      <polygon class="chevron-band" points="417,0 458,0 220,237 297,325 255,325 179,237" fill="var(--brand-grey)"/>
      <polygon class="accent-panel" points="463,0 572,0 572,325 302,325 224,237" fill="url(#panelBlue)"/>
    </svg>

    <div class="brand">
      <p class="brand__name">HUIDPUNTZORG</p>
      <p class="brand__tagline">next generation skin care</p>
    </div>

    <address class="contact" style="font-style: normal;">
      <div class="contact__group">
        <p>Lindenhoflaan 214B</p>
        <p>3041KP Rotterdam</p>
        <p>Tel 010 483 21 95</p>
      </div>
      <div class="contact__group">
        <p>Zonnewijzerstraat 238</p>
        <p>1062RT Amsterdam</p>
        <p>Tel 020 571 3829</p>
      </div>
      <div class="contact__group">
        <p class="contact__row">info@huidpuntzorg.nu
          <svg class="contact__icon" viewBox="0 0 16 16" aria-hidden="true">
            <rect x="1.5" y="3.5" width="13" height="9" fill="none" stroke="#fff" stroke-width="1.4"/>
            <polyline points="1.5,3.5 8,9 14.5,3.5" fill="none" stroke="#fff" stroke-width="1.4"/>
          </svg>
        </p>
        <p class="contact__row">www.huidpuntzorg.nu
          <svg class="contact__icon" viewBox="0 0 16 16" aria-hidden="true">
            <circle cx="8" cy="8" r="7" fill="#fff"/>
            <g fill="none" stroke="var(--blue-deep)" stroke-width="1">
              <ellipse cx="8" cy="8" rx="3" ry="6.5"/>
              <line x1="1.5" y1="8" x2="14.5" y2="8"/>
              <line x1="8" y1="1.5" x2="8" y2="14.5"/>
            </g>
          </svg>
        </p>
      </div>
    </address>
  </section>

  <section class="card card--back" aria-label="Achterkant visitekaartje">
    <div class="brand">
      <p class="brand__name">HUIDPUNTZORG</p>
      <p class="brand__tagline">next generation skin care</p>
    </div>
    <p class="website">www.huidpuntzorg.nu</p>
  </section>

</body>
</html>
```